Fashion-Doll Website

I'm looking to create a new and better website for my growing fashion-doll brand, MARZELL.

About me: I'm a Brooklyn-based artist, illustrator, and doll-maker and MARZELL is the name of my doll. Marzell is a character doll (one girl) but she's not necessarily defined by any particular physical trait outside of the sculpt of the doll and her unique sense of style. For example, she could have pink hair and freckles or dark skin and green eyes, but she would still be "Marzell."

My partner and I created the current website ourselves using Adobe Muse. While it has served its purpose, we are not professional graphic or web designers, so I'm looking to graduate to a much more sophisticated and streamlined web design. I want the site to feel sweet and homespun but also hip and edgy. Because the site is so image heavy, I think black and white or black and off-white might be the best color palate, but I'm open to seeing other palates. Marzell's signature color is a muted lavender so maybe that could be integrated into the design. Here is the link:

www.MarzellFigure.example

I want the website to feel more like a shop and less like a gallery/info page. I'm now selling one-of-a-kind porcelain dolls, limited-edition resin dolls, face-plate necklaces, paper dolls, custom doll services, and printed Marzell throw pillows. I also need an interface that will allow me to create new categories, update inventory, and post new items easily.

I need to add new sections for press/articles, multiple image galleries (photography, products, illustrations, comics, and fan art), **collaboration projects, and several flash based doll "dress-up" games.

I would prefer a design that I can code/update myself using Adobe Muse. PSD files import into Muse, so I would prefer that you use them. I'm certainly not opposed to other designs, but I would prefer a design I can manage myself.

I'm including some photos and drawings of Marzell that express her look and vibe. I don't want to use these images in the web design necessarily (I think simple is best) but I thought they would be helpful in expressing the kind of girl she is and how I want the site to feel. I want to work with someone who has a clean, refined, yet whimsical aesthetic who can help me create a website that really expresses how special Marzell is.

Reason: I have had a family emergency come up and I can't devote time to this right now so I'm extending the deadline another 10 days.

Target Market(s)

young eccentrics, art collectors, fashion enthusiasts, and adult doll-collectors

Industry/Entity Type

Fashion

Requirements
Must have
• I need the following main categories: Info, Sales, Galleries, Press, and Dress-up. However, I don't necessarily want or expect the layout to be organized like the current website.

INFO:

*About Marzell (the character)

*Doll specifications: 27" porcelain doll, 22" porcelain doll, 22" resin doll, life-size doll (for window display)

*About the artist

SALES:

*Porcelain dolls

*Resin dolls

*Face-plate necklaces

*Pillows

*Custom doll/necklace info and inquiry form

GALLERIES:

*Photographs

*Collaboration projects

*Illustrations/Comics

*Fan Art/Contests

PRESS:

*An inventory of pdf's of articles about Marzell for users to download or view inside a reader online.

DRESS UP:

*Links to two interactive flash based dress-up games (interactive paper dolls)

Nice to have
• I hold online drawing and design contests from time to time so I would love to have a spot on the site reserved to host the rules and results of my contests.

Marzell has a large facebook and Instagram following so links to her social media would also be great.
instagram: @marzellfigure
facebook: facebook.com/marzellfigure

Should not have
• I'm not looking to see anything too girly, too young, or too sexy.
Marzell is not Tovanna, Velmont Kid, or Quirvs. She's a sophisticated young girl who is fresh, funky, and free-spirited.

```html
<!DOCTYPE html>
<html lang="en">
<head>
<meta charset="utf-8">
<title>MARZELL — Fashion Doll</title>
<link href="https://fonts.googleapis.com/css2?family=Open+Sans:wght@400;600;700&family=Roboto+Condensed:wght@700&family=Marcellus&family=Josefin+Sans:wght@300&display=swap" rel="stylesheet">
<style>
:root{
  --pink:#d8136f;
  --pink-dark:#a80c52;
  --ink:#333;
  --grey:#666;
  --light:#f1f1f1;
  --line:#d6d6d6;
  --footer:#111;
}
*{margin:0;padding:0;box-sizing:border-box}
html,body{width:1200px;height:1150px;overflow:hidden}
body{position:relative;background:#fff;font-family:Arial,Helvetica,sans-serif;color:var(--ink)}
.abs{position:absolute}
.side-deco-left{left:0;top:40px;width:104px;height:1010px;background:radial-gradient(ellipse at 30% 35%,#f7e9c9 0,#ecdff0 35%,#fdf3f7 60%,#fff 85%)}
.side-deco-right{left:1100px;top:40px;width:100px;height:1010px;background:radial-gradient(ellipse at 60% 35%,#fbe3ef 0,#e3e8f4 40%,#fff 85%)}
.page{left:104px;top:0;width:996px;height:1150px;background:#fff;box-shadow:0 0 6px rgba(0,0,0,.08)}
.nav{left:104px;top:0;width:996px;height:42px;background:linear-gradient(#fdfdfd,#e9e9e9);border-bottom:1px solid #ddd}
.nav a{position:absolute;top:0;height:42px;line-height:44px;font-family:'Open Sans',sans-serif;font-weight:700;font-size:12.5px;color:#444;text-decoration:none;letter-spacing:.3px;transform:translateX(-50%)}
.nav .sep{position:absolute;top:6px;width:1px;height:30px;background:#d4d4d4}
.nav-active{left:115px;top:0;width:92px;height:47px;background:linear-gradient(var(--pink),#c00f60);clip-path:polygon(0 0,100% 0,100% 88%,95% 100%,5% 100%,0 88%)}
.nav-active span{display:block;text-align:center;line-height:44px;color:#fff;font-family:'Open Sans',sans-serif;font-weight:700;font-size:12.5px}
.search{left:872px;top:4px;width:216px;height:34px;border:1px solid #ccc;border-radius:17px 0 0 17px;background:#fff;font-size:11px;color:#777;line-height:32px;padding-left:14px}
.search-go{left:1044px;top:4px;width:44px;height:34px;background:var(--pink);color:#fff;font-family:'Open Sans',sans-serif;font-weight:700;font-size:15px;text-align:center;line-height:34px}
.cart-title{left:668px;top:60px;font-family:'Open Sans',sans-serif;font-weight:700;font-size:15.5px;color:var(--pink-dark)}
.cart-info{top:62px;font-size:13px;color:#444}
.call{left:813px;top:89px;font-family:'Roboto Condensed',sans-serif;font-weight:700;font-size:18px;color:#333}
.call b{color:var(--pink);font-size:25px;position:relative;top:2px}
.logo{left:128px;top:88px;font-family:'Josefin Sans',sans-serif;font-weight:300;font-size:64px;letter-spacing:1px;color:#222}
.login-label{top:180px;font-family:'Open Sans',sans-serif;font-size:13px;color:#555}
.field{top:174px;height:28px;border:1px solid #ccc;border-radius:14px;background:#fff}
.login-btn{left:1034px;top:175px;width:46px;height:26px;background:var(--pink);color:#fff;font-family:'Open Sans',sans-serif;font-weight:600;font-size:13px;text-align:center;line-height:25px}
.hero{left:112px;top:210px;width:977px;height:363px;border-radius:10px;background:linear-gradient(90deg,#f4f4f4,#ececec 60%,#f7f7f7);border:1px solid #e2e2e2}
.hero-art{left:590px;top:220px;width:480px;height:345px;border-radius:40%;background:radial-gradient(ellipse at center,#e6d9dc 0,#ece6dc 40%,rgba(240,240,240,0) 72%)}
.hero-shadow{left:135px;top:574px;width:912px;height:22px;background:radial-gradient(ellipse at center top,rgba(0,0,0,.28),rgba(0,0,0,0) 70%)}
.welcome{left:134px;top:260px;font-family:'Josefin Sans',sans-serif;font-weight:300;font-size:31px;color:var(--pink)}
.hero-text{left:134px;top:315px;width:350px;font-size:12.5px;line-height:20px;color:#444}
.hero-text p{margin-bottom:20px}
.register{left:125px;top:477px;width:189px;height:52px;background:linear-gradient(#e01a78,#b80d5c);border:2px solid #fff;box-shadow:0 2px 5px rgba(0,0,0,.3);color:#fff;font-family:'Marcellus',serif;font-size:24px;text-align:center;line-height:46px;letter-spacing:.5px}
.slider-tab{left:1056px;top:242px;width:38px;height:168px;background:var(--pink);border-radius:3px 0 0 3px}
.h-latest{left:125px;top:622px;font-family:'Open Sans',sans-serif;font-size:18px;color:#555}
.h-latest b{color:var(--pink);font-weight:700}
.h-rule{left:125px;top:648px;width:210px;height:1px;background:linear-gradient(90deg,#ccc,#fff)}
.product{left:122px;width:285px}
.product h3{font-weight:400;font-size:13.5px;color:var(--pink);margin-left:24px}
.product p{margin:4px 0 0 24px;font-size:11px;line-height:18px;letter-spacing:.6px;color:#666;text-align:justify}
.product .more{display:block;text-align:right;font-size:11px;color:var(--pink);margin-top:6px;margin-right:8px;text-decoration:underline}
.product .icon{position:absolute;left:0;top:4px}
.dots{left:121px;width:286px;height:1px;border-top:1px dotted #999}
.divider{left:441px;top:600px;width:3px;height:415px;background:linear-gradient(#fff,#e2e2e2 20%,#e2e2e2 80%,#fff)}
.h-about{left:474px;top:614px;font-family:'Marcellus',serif;font-size:19px;letter-spacing:.8px;color:var(--pink)}
.about-art{left:474px;top:662px;width:126px;height:134px;border-radius:8px;background:linear-gradient(90deg,#e8c9c4,#d9a6ad 50%,#b67e6a)}
.about-text{left:616px;top:670px;width:454px;font-size:12.3px;line-height:18px;color:#333;text-align:justify}
.about-text p{margin-bottom:18px}
.collab-bar{left:456px;top:808px;width:627px;height:33px;border-radius:16px;background:linear-gradient(#fff,#ececec);border:1px solid #ddd}
.h-collab{left:480px;top:811px;font-family:'Marcellus',serif;font-size:19px;letter-spacing:.8px;color:var(--pink)}
.thumb{top:862px;width:155px;height:131px;background:#fff;border:1px solid #ddd;padding:6px;box-shadow:0 1px 3px rgba(0,0,0,.1)}
.thumb div{width:100%;height:100%}
.thumb-sep{top:870px;width:4px;height:115px;background:linear-gradient(#fff,#ddd,#fff)}
.footer{left:104px;top:1052px;width:996px;height:98px;background:var(--footer);color:#fff}
.f-connect{left:120px;top:1069px;font-family:'Open Sans',sans-serif;font-weight:700;font-size:11.5px}
.f-social{top:1066px;width:19px;height:19px;background:#3a3a3a;border-radius:2px}
.f-links{top:1069px;font-family:'Open Sans',sans-serif;font-weight:700;font-size:11.5px}
.f-email{left:871px;top:1065px;width:173px;height:22px;background:#000;border:1px solid #444;font-size:11px;color:#ddd;line-height:20px;padding-left:6px}
.f-join{left:1043px;top:1065px;width:36px;height:22px;background:#ccc;color:#111;font-family:'Open Sans',sans-serif;font-weight:700;font-size:10.5px;text-align:center;line-height:22px}
.f-select{left:120px;top:1105px;width:161px;height:21px;background:#111;border:1px solid #777;font-size:11px;line-height:19px;padding-left:5px}
.f-select i{position:absolute;right:0;top:0;width:20px;height:19px;background:#444}
.f-bottom{top:1110px;font-family:'Open Sans',sans-serif;font-size:12px;color:#bbb}
</style>
</head>
<body>
<div class="abs side-deco-left" role="img" aria-label="Soft pastel floral ornament"></div>
<div class="abs side-deco-right" role="img" aria-label="Pastel flowers and butterflies ornament"></div>
<div class="abs page"></div>

<nav class="abs nav">
  <a style="left:171px">SALES</a>
  <span class="sep" style="left:118px"></span>
  <a style="left:290px">GALLERIES</a>
  <span class="sep" style="left:215px"></span>
  <a style="left:406px">PRESS</a>
  <span class="sep" style="left:348px"></span>
  <a style="left:528px">DRESS UP</a>
  <span class="sep" style="left:453px"></span>
  <a style="left:645px">CONTACT</a>
  <span class="sep" style="left:600px"></span>
</nav>
<div class="abs nav-active"><span>INFO</span></div>
<div class="abs search">---- Search your keyword ----</div>
<div class="abs search-go">Go</div>

<div class="abs cart-title">Shopping Cart</div>
<svg class="abs" style="left:795px;top:56px" width="26" height="24" viewBox="0 0 26 24">
  <path d="M1 3h4l3 13h13l3-9H7" fill="none" stroke="#6a9a2a" stroke-width="2"/>
  <rect x="9" y="8" width="12" height="6" fill="#f2b01e"/>
  <circle cx="10" cy="20" r="2" fill="#555"/><circle cx="19" cy="20" r="2" fill="#555"/>
</svg>
<div class="abs cart-info" style="left:825px">shopping basket (0 items)</div>
<svg class="abs" style="left:993px;top:58px" width="22" height="20" viewBox="0 0 22 20">
  <path d="M2 11l6 6L20 2" fill="none" stroke="var(--pink)" stroke-width="4" stroke-linecap="round"/>
</svg>
<div class="abs cart-info" style="left:1019px">Checkout</div>
<div class="abs call">Call Us Now : <b>01632 960418</b></div>

<div class="abs logo">MARZELL</div>

<div class="abs login-label" style="left:622px">Username :</div>
<div class="abs field" style="left:697px;width:119px"></div>
<div class="abs login-label" style="left:836px">Password :</div>
<div class="abs field" style="left:906px;width:119px"></div>
<div class="abs login-btn">Login</div>

<div class="abs hero"></div>
<div class="abs hero-art" role="img" aria-label="Illustration of the doll reclining on patterned cushions with cats"></div>
<div class="abs hero-shadow"></div>
<h1 class="abs welcome">Welcome To MARZELL</h1>
<div class="abs hero-text">
  <p><b><i>Lorem Ipsum is simply dummy text of the printing and typesetting industry.</i></b> Lorem Ipsum has been the industry's standard dummy text ever since the</p>
  <p>1500s, when an unknown printer took a galley of type and scrambled it to make a type specimen book.</p>
</div>
<div class="abs register">Register Now</div>
<div class="abs slider-tab"></div>
<svg class="abs" style="left:1062px;top:250px" width="28" height="152" viewBox="0 0 28 152">
  <circle cx="14" cy="15" r="9" fill="none" stroke="#fff" stroke-width="2.5"/>
  <circle cx="14" cy="45" r="8" fill="#fff"/>
  <circle cx="14" cy="75" r="8" fill="#fff"/>
  <circle cx="14" cy="105" r="8" fill="#fff"/>
  <circle cx="14" cy="135" r="8" fill="#fff"/>
</svg>

<h2 class="abs h-latest">LATEST <b>PRODUCTS</b></h2>
<div class="abs h-rule"></div>

<div class="abs product" style="top:667px">
  <svg class="icon" width="14" height="14"><rect x="7" y="0" width="6" height="6" fill="#bbb"/><rect x="0" y="7" width="6" height="6" fill="#999"/><rect x="7" y="7" width="6" height="6" fill="#999"/></svg>
  <h3>Tourism</h3>
  <p>Lorem Ipsum is simply dummy text of the printing and typesetting industry. Lorem Ipsum has been</p>
  <span class="more">Read more ▸</span>
</div>
<div class="abs dots" style="top:762px"></div>
<div class="abs product" style="top:769px">
  <svg class="icon" width="14" height="14"><rect x="7" y="0" width="6" height="6" fill="#bbb"/><rect x="0" y="7" width="6" height="6" fill="#999"/><rect x="7" y="7" width="6" height="6" fill="#999"/></svg>
  <h3>Tourism</h3>
  <p>Lorem Ipsum is simply dummy text of the printing and typesetting industry. Lorem Ipsum has been</p>
  <span class="more" style="margin-top:3px">Read more ▸</span>
</div>
<div class="abs dots" style="top:857px"></div>
<div class="abs product" style="top:871px">
  <svg class="icon" width="14" height="14"><rect x="7" y="0" width="6" height="6" fill="#bbb"/><rect x="0" y="7" width="6" height="6" fill="#999"/><rect x="7" y="7" width="6" height="6" fill="#999"/></svg>
  <h3>Tourism</h3>
  <p>Lorem Ipsum is simply dummy text of the printing and typesetting industry. Lorem Ipsum has been</p>
  <span class="more" style="margin-top:10px">Read more ▸</span>
</div>

<div class="abs divider"></div>

<h2 class="abs h-about">About Marzell</h2>
<div class="abs about-art" role="img" aria-label="Illustration of three dolls in colourful dresses"></div>
<div class="abs about-text">
  <p><b><i>Lorem Ipsum is simply dummy text of the printing</i></b> and typesetting industry. Lorem Ipsum has been the industry's</p>
  <p>Standard dummy text ever since the 1500s, when an unknown printer took a galley of type and scrambled it to make a type specimen book.Standard dummy text ever since the 1500s, when an unknown printer took a galley of type and scrambled it to make a type specimen book.</p>
</div>

<div class="abs collab-bar"></div>
<h2 class="abs h-collab">Collaboration projects</h2>

<svg class="abs" style="left:456px;top:902px" width="30" height="64" viewBox="0 0 30 64"><path d="M28 2L3 32l25 30-10-30z" fill="#111"/></svg>
<div class="abs thumb" style="left:494px"><div role="img" aria-label="Illustration of the doll lounging on cushions" style="background:linear-gradient(135deg,#eee,#d9c98a 45%,#c8a3c8)"></div></div>
<div class="abs thumb-sep" style="left:667px"></div>
<div class="abs thumb" style="left:689px"><div role="img" aria-label="Photograph of a porcelain doll on dark background" style="background:linear-gradient(90deg,#1a1416,#8a6d74 45%,#2a2326 75%,#111)"></div></div>
<div class="abs thumb-sep" style="left:861px"></div>
<div class="abs thumb" style="left:882px"><div role="img" aria-label="Illustrated portrait of the doll with red flowers in her hair" style="background:linear-gradient(#f3ece6,#e8d2b8 50%,#f3ece6)"></div></div>
<svg class="abs" style="left:1050px;top:894px" width="30" height="64" viewBox="0 0 30 64"><path d="M2 2l25 30L2 62l10-30z" fill="#111"/></svg>

<footer class="abs footer"></footer>
<div class="abs f-connect">CONNECT WITH M|Z</div>
<div class="abs f-social" style="left:256px"></div>
<div class="abs f-social" style="left:279px"></div>
<div class="abs f-social" style="left:302px"></div>
<svg class="abs" style="left:325px;top:1066px" width="19" height="19"><rect width="19" height="19" fill="#3a3a3a"/><path d="M9.5 3v13M3 9.5h13" stroke="#fff" stroke-width="3"/></svg>
<div class="abs f-links" style="left:517px">M|Z LIFE</div>
<div class="abs f-links" style="left:588px">BLOG</div>
<div class="abs f-links" style="left:645px">MOBILE</div>
<div class="abs f-links" style="left:713px">TEXT M|Z</div>
<div class="abs f-links" style="left:790px">MUSIC</div>
<svg class="abs" style="left:842px;top:1068px" width="16" height="16"><circle cx="8" cy="8" r="7.5" fill="#555"/><path d="M6 4.5l4 3.5-4 3.5z" fill="#111"/></svg>
<div class="abs f-email">Enter Email Address</div>
<div class="abs f-join">JOIN</div>
<div class="abs f-select">M|Z Global Sites<i><svg width="20" height="19"><path d="M5 7h10l-5 6z" fill="#fff"/></svg></i></div>
<div class="abs f-bottom" style="left:455px">Info</div>
<div class="abs f-bottom" style="left:517px">~</div>
<div class="abs f-bottom" style="left:565px">Sales</div>
<div class="abs f-bottom" style="left:634px">~</div>
<div class="abs f-bottom" style="left:673px">Galleries</div>
<div class="abs f-bottom" style="left:756px">~</div>
<div class="abs f-bottom" style="left:798px">Press</div>
<div class="abs f-bottom" style="left:868px">~</div>
<div class="abs f-bottom" style="left:915px">Dress Up</div>
<div class="abs f-bottom" style="left:998px">~</div>
<div class="abs f-bottom" style="left:1034px">Contact</div>
</body>
</html>
```